Business Card for Academic Coach

I need a business card designed for me - a private tutor/academic coach.

Glen Marlowe
Academic Coach
AB Velden University, 1994 Cum Laude
Phone: 555-317-8842
glenmmarlowe@quillpost.example

Subjects
SAT and ACT
Math, Physics, Writing

Industry/Entity Type

Business

```html
<!DOCTYPE html>
<html lang="en">
<head>
<meta charset="utf-8">
<title>Glen Marlowe – Academic Coach</title>
<link rel="stylesheet" href="https://fonts.googleapis.com/css2?family=Archivo:ital,wght@0,700;1,700&display=swap">
<style>
  :root {
    --navy: #011443;
    --navy-soft: #0c2a5a;
    --navy-faint: #08214f;
    --sky: #1ea8ec;
    --rule: #d4562e;
    --white: #ffffff;
  }
  html, body {
    margin: 0;
    padding: 0;
    overflow: hidden;
    background: var(--navy);
  }
  .card {
    position: relative;
    width: 1200px;
    height: 685px;
    background: var(--navy);
    overflow: hidden;
    font-family: "Archivo", Arial, sans-serif;
  }
  .card__backdrop {
    position: absolute;
    left: 24px;
    top: 18px;
    width: 744px;
    height: 648px;
    border-radius: 40px;
    background: radial-gradient(ellipse at 45% 45%, var(--navy-soft) 0%, var(--navy-faint) 55%, rgba(1, 20, 67, 0) 80%);
  }
  .card__name {
    position: absolute;
    left: 420px;
    top: 232px;
    margin: 0;
    color: var(--sky);
    font-weight: 700;
    font-size: 100px;
    line-height: 88px;
    letter-spacing: -1px;
  }
  .card__name span {
    display: block;
  }
  .card__rule {
    position: absolute;
    left: 420px;
    top: 435px;
    width: 780px;
    height: 2px;
    background: var(--rule);
  }
  .card__title {
    position: absolute;
    left: 420px;
    top: 446px;
    margin: 0;
    color: var(--white);
    font-style: italic;
    font-weight: 700;
    font-size: 40px;
    letter-spacing: 1px;
  }
</style>
</head>
<body>
  <div class="card">
    <div class="card__backdrop" role="img" aria-label="Faint illustration of a graduation cap above a rolled diploma tied with a ribbon"></div>
    <h1 class="card__name"><span>Glen</span><span>Marlowe</span></h1>
    <div class="card__rule"></div>
    <p class="card__title">Academic Coach</p>
  </div>
</body>
</html>
```